uKidShelter Advert, internet security for children.

we need a newspaper/magazine advert approx. size 150mm wide by 110mm high

uKidShelter is a service used to protect children online when using all types of devices, on Wi-Fi and mobile network connections.

the website is www.ukidshelter.co.uk

The ad should communicate ease of use, and should be aimed at parents with children between the ages of 3-18

attached logo designs.

Target Market(s)

Parents with children aged 3-18

Industry/Entity Type

Internet

Font styles to use
Serif
Sans Serif

Requirements
Must have
• company logo, website address, platforms service works on, android, iOS etc. free 30 day trial.
Nice to have
• email address of info@ukidshelter.co.uk
Should not have
• phone numbers, pricing.

```html
<!DOCTYPE html>
<html lang="en">
<head>
<meta charset="utf-8">
<title>uKidShelter Advert</title>
<link rel="stylesheet" href="https://fonts.googleapis.com/css2?family=Archivo+Black&family=Questrial&family=Montserrat:wght@700&display=swap">
<style>
  :root {
    --blue-bright: #1a9ad6;
    --blue-mid: #12689f;
    --blue-deep: #0b3a5c;
    --accent: #4fc3f0;
    --navy: #163c66;
    --white: #ffffff;
    --frame: #d9dde2;
  }
  html, body {
    margin: 0;
    padding: 0;
    overflow: hidden;
    background: #e9ecef;
  }
  .advert {
    position: relative;
    width: 1200px;
    height: 878px;
    overflow: hidden;
    background: radial-gradient(ellipse at 35% 0%, var(--blue-bright) 0%, var(--blue-mid) 45%, var(--blue-deep) 100%);
    font-family: "Questrial", sans-serif;
    color: var(--white);
  }
  .photo-cloud {
    position: absolute;
    left: 0;
    top: 0;
    width: 1200px;
    height: 878px;
  }
  .brand-box {
    position: absolute;
    left: 716px;
    top: 16px;
    width: 484px;
    height: 133px;
    background: var(--white);
    border-radius: 22px 0 0 22px;
    display: flex;
    align-items: center;
    justify-content: center;
    gap: 18px;
  }
  .brand-dot {
    width: 46px;
    height: 46px;
    border-radius: 50%;
    background: var(--navy);
  }
  .brand-name {
    font-family: "Questrial", sans-serif;
    font-size: 50px;
    color: var(--navy);
  }
  .headline {
    position: absolute;
    right: 40px;
    top: 176px;
    margin: 0;
    text-align: right;
    font-family: "Archivo Black", sans-serif;
    font-weight: 400;
    font-size: 46px;
    line-height: 56px;
    color: var(--white);
    text-shadow:
      -2px -2px 0 var(--blue-deep), 2px -2px 0 var(--blue-deep),
      -2px 2px 0 var(--blue-deep), 2px 2px 0 var(--blue-deep),
      3px 4px 3px rgba(0,0,0,0.5);
  }
  .feature {
    position: absolute;
    right: 40px;
    display: flex;
    align-items: center;
    gap: 14px;
    text-align: right;
    font-size: 37px;
    line-height: 40px;
  }
  .feature--easy { top: 340px; }
  .feature--safe { top: 448px; }
  .feature svg { flex: none; }
  .trial {
    position: absolute;
    right: 40px;
    top: 566px;
    text-align: right;
  }
  .trial-free {
    font-family: "Montserrat", sans-serif;
    font-weight: 700;
    font-size: 44px;
    line-height: 46px;
    color: var(--accent);
  }
  .trial-days {
    font-size: 36px;
    line-height: 40px;
  }
  .contact {
    position: absolute;
    right: 40px;
    top: 690px;
    text-align: right;
  }
  .contact-lead {
    font-size: 22px;
    line-height: 28px;
    color: var(--accent);
  }
  .contact-web,
  .contact-email {
    font-size: 26px;
    line-height: 32px;
    letter-spacing: 0.5px;
  }
  .platforms {
    position: absolute;
    right: 40px;
    top: 800px;
    display: flex;
    gap: 22px;
  }
  .platform {
    display: flex;
    flex-direction: column;
    align-items: center;
    width: 64px;
    gap: 4px;
    font-size: 14px;
    line-height: 16px;
    color: var(--white);
  }
  .platform-mark {
    width: 38px;
    height: 38px;
    border-radius: 50%;
    background: var(--accent);
  }
</style>
</head>
<body>
<main class="advert">
  <svg class="photo-cloud" viewBox="0 0 1200 878">
    <defs>
      <linearGradient id="photoTones" x1="0" y1="0" x2="1" y2="1">
        <stop offset="0" stop-color="#c9a48f"/>
        <stop offset="0.45" stop-color="#d98a9c"/>
        <stop offset="0.75" stop-color="#6b8fbf"/>
        <stop offset="1" stop-color="#e4ddd2"/>
      </linearGradient>
    </defs>
    <path role="img" aria-label="Photo of four smiling children using mobile phones together"
      d="M0,150 C60,90 150,52 240,60 C320,68 370,120 395,190 C470,185 540,250 548,330 C640,350 722,440 712,560 C762,620 782,720 742,878 L0,878 Z"
      fill="url(#photoTones)" stroke="var(--frame)" stroke-width="12"/>
  </svg>

  <div class="brand-box">
    <span class="brand-dot"></span>
    <span class="brand-name">uKidShelter</span>
  </div>

  <h1 class="headline">Protect your children<br>from the web.</h1>

  <div class="feature feature--easy">
    <svg width="78" height="78" viewBox="0 0 78 78" aria-hidden="true">
      <circle cx="39" cy="39" r="35" fill="none" stroke="var(--accent)" stroke-width="4"/>
      <path d="M22 40 L35 53 L57 24" fill="none" stroke="var(--accent)" stroke-width="6" stroke-linecap="round" stroke-linejoin="round"/>
    </svg>
    <span>Easy to use</span>
  </div>

  <div class="feature feature--safe">
    <svg width="70" height="78" viewBox="0 0 70 78" aria-hidden="true">
      <path d="M35 4 C24 10 14 12 5 12 L5 36 C5 56 18 68 35 74 C52 68 65 56 65 36 L65 12 C56 12 46 10 35 4 Z" fill="none" stroke="var(--accent)" stroke-width="4" stroke-linejoin="round"/>
    </svg>
    <span>Safe for<br>children</span>
  </div>

  <div class="trial">
    <div class="trial-free">FREE 30</div>
    <div class="trial-days">days trial</div>
  </div>

  <div class="contact">
    <div class="contact-lead">For more info visit us</div>
    <div class="contact-web">www.ukidshelter.co.uk</div>
    <div class="contact-email">info@ukidshelter.co.uk</div>
  </div>

  <div class="platforms" aria-label="Works on all your devices">
    <div class="platform"><span class="platform-mark"></span>Phone</div>
    <div class="platform"><span class="platform-mark"></span>Tablet</div>
    <div class="platform"><span class="platform-mark"></span>Laptop</div>
    <div class="platform"><span class="platform-mark"></span>Desktop</div>
  </div>
</main>
</body>
</html>
```